Book Cover design for book about character and ethics

This is an exciting book about what it means to live an authentic life. It revolves around finding a sense of contentment, solid friendships and being a good person. The idea is to move away from chasing excessive wealth, good looks and popularity in order to find happiness. Authentic happiness requires a different chase. This book is also about a solid foundation, priorities and work / life balance.

I want a cover that is CREATIVE and POPS. It needs to stand out on the shelf from other books.

Target Market(s)

High school, college and working professionals.

Font styles to use
Serif

Requirements
Must have
• Title: True Otters: Seek A Grounded Path
• Author Name: Dana Vellamore
• Creativity - makes the point without being entirely obvious
• Cover must pop in comparison to other books
• Use bright colors
• Easy to read text
• Cool picture or vector art
Nice to have
• Topics to think about:
• 1. Stand out from the crowd
• 2. The world is lying to you about what makes you happy
• 3. Renewal
• 4. Rebuild
• 5. Chase What Matters
• 6. Pushing against the wind
• I included some pics below as guidance
Should not have
• Cannot be cheesy
• Do not put a rabbit on the cover even though the book is called "True Otters"

```html
<!DOCTYPE html>
<html lang="en">
<head>
<meta charset="utf-8">
<title>True Otters: Seek A Grounded Path</title>
<link rel="stylesheet" href="https://fonts.googleapis.com/css2?family=Gochi+Hand&family=Didact+Gothic&family=Montserrat:wght@500&display=swap">
<style>
  :root {
    --sky: #f1ede6;
    --facade-light: #e6ddd0;
    --facade-warm: #cdbba4;
    --facade-shadow: #7d7468;
    --street: #c9c6c2;
    --street-deep: #9c9894;
    --figure-tone: #8a8f96;
    --figure-deep: #3f3a3a;
    --skin-warm: #e3b99a;
    --stroke-top: #f6a23c;
    --stroke-mid: #f27433;
    --stroke-bottom: #ec4f5e;
    --title: #ffffff;
    --subtitle: #3a3331;
    --author: #1f1f1f;
  }
  html, body {
    margin: 0;
    padding: 0;
    width: 849px;
    height: 1200px;
    overflow: hidden;
    background: #ffffff;
  }
  .cover {
    position: relative;
    width: 849px;
    height: 1200px;
    overflow: hidden;
  }
  .cover-photo {
    position: absolute;
    inset: 0;
    background:
      radial-gradient(ellipse 130px 300px at 600px 640px, rgba(63,58,58,0.55), transparent 75%),
      radial-gradient(ellipse 150px 220px at 610px 560px, rgba(138,143,150,0.55), transparent 75%),
      radial-gradient(ellipse 170px 120px at 780px 600px, rgba(63,58,58,0.5), transparent 75%),
      radial-gradient(ellipse 90px 260px at 620px 1000px, rgba(227,185,154,0.6), transparent 75%),
      radial-gradient(ellipse 60px 200px at 500px 220px, rgba(227,185,154,0.5), transparent 75%),
      radial-gradient(ellipse 80px 180px at 780px 260px, rgba(227,185,154,0.45), transparent 75%),
      radial-gradient(ellipse 260px 380px at 760px 180px, var(--facade-light), transparent 80%),
      linear-gradient(90deg, var(--facade-shadow) 0%, var(--facade-warm) 45%, var(--facade-light) 62%, var(--facade-shadow) 72%, var(--facade-light) 85%, var(--facade-warm) 100%);
  }
  .cover-photo::after {
    content: "";
    position: absolute;
    inset: 0;
    background: linear-gradient(180deg, transparent 0%, transparent 55%, rgba(201,198,194,0.85) 75%, var(--street) 100%);
  }
  .brush-stroke {
    position: absolute;
    left: 0;
    top: 0;
    width: 849px;
    height: 1200px;
  }
  .title {
    position: absolute;
    left: 78px;
    top: 700px;
    margin: 0;
    font-family: "Gochi Hand", cursive;
    font-weight: 400;
    font-size: 112px;
    line-height: 100px;
    letter-spacing: 2px;
    color: var(--title);
    text-transform: uppercase;
  }
  .subtitle {
    position: absolute;
    left: 80px;
    top: 945px;
    margin: 0;
    font-family: "Didact Gothic", sans-serif;
    font-size: 31px;
    word-spacing: -2px;
    color: var(--subtitle);
  }
  .author {
    position: absolute;
    left: 583px;
    top: 1117px;
    margin: 0;
    font-family: "Montserrat", sans-serif;
    font-weight: 500;
    font-size: 14px;
    letter-spacing: 1.5px;
    color: var(--author);
    text-transform: uppercase;
  }
</style>
</head>
<body>
  <main class="cover">
    <div class="cover-photo" role="img" aria-label="Photograph of a young woman with a ponytail and backpack walking down a sunny city street, arms raised in joy"></div>

    <svg class="brush-stroke" viewBox="0 0 849 1200" aria-hidden="true">
      <defs>
        <linearGradient id="strokeFill" x1="0" y1="0" x2="0" y2="1">
          <stop offset="0" stop-color="var(--stroke-top)" stop-opacity="0.82"/>
          <stop offset="0.45" stop-color="var(--stroke-mid)" stop-opacity="0.9"/>
          <stop offset="1" stop-color="var(--stroke-bottom)" stop-opacity="0.97"/>
        </linearGradient>
        <linearGradient id="streakFill" x1="0" y1="0" x2="0" y2="1">
          <stop offset="0" stop-color="var(--stroke-top)" stop-opacity="0.55"/>
          <stop offset="1" stop-color="var(--stroke-mid)" stop-opacity="0"/>
        </linearGradient>
      </defs>
      <path fill="url(#strokeFill)"
        d="M0 0 H390 L398 80 L410 170 L424 260 L440 350 L458 440 L476 530 L490 620 L500 710 L505 800 L504 880 L498 960 L488 1040 L476 1120 L466 1200 H0 Z"/>
      <path fill="url(#streakFill)"
        d="M390 0 H440 L446 90 L456 180 L468 270 L476 360 L470 420 L456 330 L442 240 L428 150 L412 70 Z"/>
    </svg>

    <h1 class="title">True<br>Otters</h1>
    <p class="subtitle">Seek A Grounded Path</p>
    <p class="author">Dana Vellamore</p>
  </main>
</body>
</html>
```